Hop Grower Producer Card

A wisconsin based grower of high quality mid westrn grown Hops with the concept of growing and processing Hops into pellet form for sale to brewers of beer large and small .varieties are grown are Cascade ,Chinook and Centennial

Target Market(s)

Brew masters at micro brews and large breweries

Industry/Entity Type

Processing

Font styles to use
Decorative
Script

Requirements
Must have
• i would like the Hop varieties listed on the back of the card , with the statement Grower of High Quality Wisconsin Hops and the web site address
Nice to have
• german style font for the name Velmar's Bine Hollow

```html
<!DOCTYPE html>
<html lang="en">
<head>
<meta charset="utf-8">
<title>Velmar's Bine Hollow – Business Cards</title>
<link href="https://fonts.googleapis.com/css2?family=Arimo:wght@400;700&display=swap" rel="stylesheet">
<style>
  :root {
    --page: #ecebe6;
    --card-green: #114a35;
    --card-green-deep: #0b3a29;
    --title-cream: #e6efc9;
    --accent-yellow: #f2c21b;
    --text-light: #f4f7ec;
    --hop-light: #b7d67a;
    --hop-mid: #6f9e3a;
    --hop-dark: #2f5a22;
  }
  * { box-sizing: border-box; margin: 0; padding: 0; }
  html, body { width: 1200px; height: 1000px; overflow: hidden; }
  body {
    background: var(--page);
    display: flex;
    flex-direction: column;
    align-items: center;
    justify-content: center;
    gap: 60px;
    font-family: "Arimo", Arial, sans-serif;
  }
  .card {
    position: relative;
    width: 740px;
    height: 423px;
    background: var(--card-green);
    overflow: hidden;
    box-shadow: 0 6px 18px rgba(0,0,0,0.18);
  }
  .card-title {
    position: absolute;
    font-family: "Arimo", Arial, sans-serif;
    font-weight: 700;
    color: var(--title-cream);
    font-size: 50px;
    line-height: 1;
    white-space: nowrap;
  }

  /* Back card */
  .back .hop-photo {
    position: absolute; inset: 0;
    background:
      radial-gradient(ellipse at 58% 48%, var(--hop-light) 0%, var(--hop-mid) 22%, transparent 48%),
      radial-gradient(ellipse at 85% 25%, #f0c040 0%, transparent 12%),
      radial-gradient(ellipse at 30% 80%, var(--hop-dark) 0%, transparent 55%),
      linear-gradient(135deg, var(--card-green-deep) 0%, var(--hop-dark) 45%, #1d4420 100%);
  }
  .back .card-title { left: 28px; top: 30px; }
  .back .tagline {
    position: absolute; left: 40px; top: 118px;
    color: var(--accent-yellow);
    font-size: 25px; font-weight: 700; line-height: 1.2;
  }
  .back .varieties {
    position: absolute; left: 56px; top: 200px;
    list-style: none;
    color: var(--accent-yellow);
    font-size: 27px; font-weight: 700; line-height: 1.45;
  }
  .back .varieties li::before { content: "• "; }
  .back .web {
    position: absolute; right: 26px; bottom: 22px;
    color: var(--text-light); font-size: 22px;
  }

  /* Front card */
  .front .hop-photo {
    position: absolute; left: 0; bottom: 0;
    width: 420px; height: 300px;
    background:
      radial-gradient(ellipse at 55% 55%, var(--hop-light) 0%, var(--hop-mid) 30%, transparent 62%),
      linear-gradient(160deg, var(--card-green) 0%, var(--hop-dark) 40%, #3f7a2a 100%);
    -webkit-mask-image: linear-gradient(to right, #000 70%, transparent 100%);
    mask-image: linear-gradient(to right, #000 70%, transparent 100%);
  }
  .front .card-title { left: 28px; top: 30px; }
  .front .contact {
    position: absolute; right: 30px; top: 110px;
    color: var(--text-light); text-align: left;
    font-style: normal;
    font-size: 19px; line-height: 1.32;
  }
  .front .person-name { font-size: 28px; font-weight: 400; }
  .front .person-role { font-size: 19px; margin-bottom: 18px; }
</style>
</head>
<body>
  <section class="card back">
    <div class="hop-photo" role="img" aria-label="Photograph of green hop cones on the bine with a glass of golden beer"></div>
    <h1 class="card-title">Velmar's Bine Hollow</h1>
    <p class="tagline">Grower of High Quality<br>Wisconsin Hops</p>
    <ul class="varieties">
      <li>Cascade</li>
      <li>Chinook</li>
      <li>Centenial</li>
    </ul>
    <p class="web">www.binehollow7.com</p>
  </section>

  <section class="card front">
    <div class="hop-photo" role="img" aria-label="Photograph of a cluster of fresh green hop cones among leaves"></div>
    <h1 class="card-title">Velmar's Bine Hollow</h1>
    <address class="contact">
      <div class="person-name">Tom Velmar</div>
      <div class="person-role">Owner / Manager</div>
      <div>214 Orchard Lane</div>
      <div>Millbrook, WI 54000</div>
      <div>Cell: 715 555 0142</div>
      <div>Fax: 715 555 0187</div>
      <div>binehollow7@mail.com</div>
      <div>www.binehollow7.com</div>
    </address>
  </section>
</body>
</html>
```